HBL Corporate Identity

As the first stage of implementing a new corporate identity we need a logo, letterhead and business card design.

The Harbourline Residents Alliance of Australia Inc (HBL) is a non-profit, volunteer-run association representing owners of strata-titled residential developments. We provide education, information and lobbying to improve the management of apartment complexes and the lives of those living in them. We’re all about “owners helping owners”. More information on our organisation can be seen at www.hbl.org.au.

The logo will be used on our own stationery and promotional materials. It will also be provided to our sponsors for use on their collateral – as such it needs to be of a ‘standard’ size so it can be easily used in a wide of materials.

Once we have chosen the new logo and corresponding design concept we will open a new contest for a complementary layout design for our website.
Updates

Thank you to everyone who submitted designs for us. There were many really great concepts, and we appreciate the effort that everyone went to - but as you know we can only choose one.

Kind regards
Margot

Target Market(s)

The primary audience is Owners of residential apartments - both resident owners and investor owners.

Secondary audiences – current and potential sponsors; organisations providing products & services to Owners Corporations & Body Corporates

Industry/Entity Type

Non-Profit

Requirements
Must have
• The design and colours should reflect a sense of community, coupled with authority, professionalism and knowledge.

We are open to all ideas.

```html
<!DOCTYPE html>
<html lang="en">
<head>
<meta charset="utf-8">
<title>HBL Stationery</title>
<link href="https://fonts.googleapis.com/css2?family=Roboto+Condensed:wght@400;700&family=Open+Sans:wght@400;600&display=swap" rel="stylesheet">
<style>
  :root {
    --backdrop: #58585c;
    --paper: #ffffff;
    --brand-green: #7cc122;
    --ink: #3a3a3c;
    --ink-soft: #6a6a6e;
    --card-edge: #c9c9cc;
    --card-shadow: #e4e4e6;
  }
  * { margin: 0; padding: 0; box-sizing: border-box; }
  html, body { width: 1200px; height: 1200px; overflow: hidden; }
  body { background: var(--backdrop); position: relative; font-family: "Open Sans", sans-serif; color: var(--ink); }

  .envelope { position: absolute; left: 80px; top: 154px; width: 1027px; height: 663px; background: var(--paper); }
  .envelope-brand { position: absolute; right: 48px; top: 52px; text-align: right; }
  .wordmark { font-family: "Roboto Condensed", sans-serif; font-weight: 700; color: var(--brand-green); line-height: 1; letter-spacing: 1px; }
  .envelope-brand .wordmark { font-size: 58px; }
  .envelope-brand .address { font-family: "Roboto Condensed", sans-serif; font-size: 8px; color: var(--ink-soft); margin-top: 8px; }

  .card-shadow { position: absolute; left: 370px; top: 363px; width: 418px; height: 215px; background: var(--card-shadow); border-radius: 6px; }
  .business-card { position: absolute; left: 380px; top: 338px; width: 417px; height: 228px; background: var(--paper); border: 1px solid var(--card-edge); border-radius: 10px; }
  .card-brand { position: absolute; left: 0; right: 0; top: 28px; text-align: center; }
  .card-brand .wordmark { font-size: 60px; }
  .card-brand .org-name { font-family: "Roboto Condensed", sans-serif; font-weight: 700; font-size: 9px; color: var(--ink); margin-top: 6px; }
  .holder { position: absolute; left: 35px; top: 110px; }
  .holder-name { font-size: 11px; color: #1e1e20; }
  .holder-role { font-size: 5.5px; letter-spacing: 1.4px; text-transform: uppercase; color: var(--ink-soft); margin-top: 1px; }
  .contacts { position: absolute; left: 38px; top: 146px; display: grid; grid-template-columns: 133px auto; row-gap: 5px; font-size: 9px; color: var(--ink-soft); }
  .contacts span b { font-weight: 600; font-size: 6px; display: inline-block; width: 14px; color: var(--ink); }
  .contacts .email { color: var(--ink); font-size: 10px; }
  .card-address { position: absolute; left: 35px; top: 191px; font-family: "Roboto Condensed", sans-serif; font-size: 10.5px; color: var(--ink); }

  .letterhead { position: absolute; left: 36px; top: 817px; width: 1133px; height: 400px; background: var(--paper); }
  .letterhead-brand { position: absolute; left: 27px; top: 18px; }
  .letterhead-brand .wordmark { font-size: 34px; }
  .letterhead-brand .org-name { font-family: "Roboto Condensed", sans-serif; font-weight: 700; font-size: 11px; color: var(--ink-soft); margin-top: 12px; }
  .letterhead-brand .address { font-family: "Roboto Condensed", sans-serif; font-size: 9.5px; color: var(--ink); margin-top: 7px; }
</style>
</head>
<body>
  <section class="envelope">
    <div class="envelope-brand">
      <div class="wordmark">HBL</div>
      <div class="address">418 Kestrel Parade,&nbsp; Lindfield NSW&nbsp; 2070 Australia</div>
    </div>
  </section>

  <div class="card-shadow"></div>
  <section class="business-card">
    <div class="card-brand">
      <div class="wordmark">HBL</div>
      <div class="org-name">Harbourline Residents Alliance of Australia Inc.</div>
    </div>
    <div class="holder">
      <div class="holder-name">Daniel R. Hale</div>
      <div class="holder-role">Operations Manager</div>
    </div>
    <div class="contacts">
      <span><b>T</b>+61 [0]422 5550187</span>
      <span><b>F</b>+61 [0]422 5550187</span>
      <span><b>M</b>+61 [0]422 5550187</span>
      <span><b>E</b><span class="email">dhale@mailbox.com</span></span>
    </div>
    <div class="card-address">418 Kestrel Parade,&nbsp; Lindfield NSW&nbsp; 2070 Australia</div>
  </section>

  <section class="letterhead">
    <div class="letterhead-brand">
      <div class="wordmark">HBL</div>
      <div class="org-name">Harbourline Residents Alliance of Australia Inc.</div>
      <div class="address">418 Kestrel Parade,&nbsp; Lindfield NSW&nbsp; 2070 Australia</div>
    </div>
  </section>
</body>
</html>
```